Design signage for shop front glass windows

Our clinic is called Wattlebrook Medical Practice and we are a general practice offering medical services. Our services include
1. General Practice Consultations
2. Immunisations
3. Health checks
4. Women's health
5. Men's Health
6. Skin cancer checks
7. Travel medicine
8. Referrals
9. Antenatal checks
10. Minor surgery
11. Cosmetic medicine
12. Pre Employment Medicals
13. Diabetes care
14. Wound care
and much more

Our motto is
"friendly and professional health care for you and your family"

We also have a range of allied health services
including
Psychology
Physiotherapy
Podiatry
Dietetics and Nutrition
Exercise Physiology
Diabetes Education

On the signs there should be the words "Bulk Billing for GP services'
"Book online at www.wattlebrookmedicalpractice.example.au"
"Ph: 07 5196 4208"

We have glass windows on our shopfront - there are 11 panels (see attached photos) - 3 panels on the left have a white film and 4 panels in the centre are just tinted (no further signage will be installed on the central glass doors which are not included). There are another 4 panels on the right that have a white film. We are looking for a design for the glass signage to promote our services. We will print signage that can be stuck on the glass. There will need to be more bold signage on the white film and more subtle minor signage on the tinted glass windows which can still allow light thru. I have attached pictures of the window. Our logo is on our website www.wattlebrookmedicalpractice.example.au to get an idea of colours.

Target Market(s)

Young families living in the region of Capalaba Queensland

Industry/Entity Type

Health Care

Font styles to use
Serif

Colors
85abd2
acd036
ec1f27

Requirements
Must have
• The words
• "Bulk Billing for General Practice Services"
• "friendly and professional health care for you and your family"
• Book online at www.wattlebrookmedicalpractice.example.au
• Phone 07 5196 4208

```html
<!DOCTYPE html>
<html lang="en">
<head>
<meta charset="utf-8">
<title>Wattlebrook Medical Practice – Centre Window Banners</title>
<link rel="stylesheet" href="https://fonts.googleapis.com/css2?family=Ubuntu:wght@400;500;700&family=Tinos&display=swap">
<style>
  :root {
    --page-bg: #ffffff;
    --panel-dark: #3f3f3f;
    --panel-light: #5a5a5a;
    --ink: #ffffff;
    --note-ink: #111111;
    --green: #acd036;
    --blue: #85abd2;
    --tick: #acd036;
  }
  * { margin: 0; padding: 0; box-sizing: border-box; }
  html, body { width: 1200px; height: 657px; overflow: hidden; background: var(--page-bg); }
  .canvas { position: relative; width: 1200px; height: 657px; font-family: "Ubuntu", sans-serif; color: var(--ink); }

  .brief-note { position: absolute; left: 0; width: 1232px; top: 30px; text-align: center; font-family: "Tinos", serif; font-size: 23px; color: var(--note-ink); }
  .panel-label { position: absolute; width: 246px; text-align: center; font-family: "Tinos", serif; font-size: 23px; color: var(--note-ink); }

  .banner { position: absolute; top: 126px; width: 246px; height: 428px;
    background: radial-gradient(ellipse 90% 60% at 85% 5%, var(--panel-light) 0%, var(--panel-dark) 70%); }
  .banner--c1 { left: 40px; }
  .banner--c2 { left: 299px; }
  .banner--c3 { left: 622px; }
  .banner--c4 { left: 880px; }
  .accent { color: var(--green); }

  .motto { position: absolute; left: 29px; top: 118px; font-size: 30.5px; font-weight: 700; line-height: 38.6px; letter-spacing: 0.2px; }

  .offer { position: absolute; left: 33px; top: 122px; font-size: 31px; font-weight: 700; line-height: 38.7px; }
  .booking { position: absolute; left: 32px; top: 250px; }
  .booking__lead { font-size: 21px; font-weight: 500; color: var(--blue); line-height: 26px; }
  .booking__url { font-size: 11.2px; font-weight: 500; margin-top: 2px; }
  .booking__phone { font-size: 16px; font-weight: 500; margin-top: 3px; }

  .list-title { font-weight: 700; color: var(--green); text-transform: uppercase; }
  .services { position: absolute; left: 36px; top: 55px; }
  .services .list-title { font-size: 18px; line-height: 20px; margin-bottom: 6px; }
  .allied { position: absolute; left: 36px; top: 51px; }
  .allied .list-title { font-size: 14.4px; line-height: 15.4px; margin-bottom: 6px; }

  .tick-list { list-style: none; }
  .tick-list li { position: relative; padding-left: 18px; font-size: 12.6px; font-weight: 500; line-height: 13px; margin-bottom: 6.5px; }
  .tick-list li svg { position: absolute; left: 0; top: 1px; width: 11px; height: 11px; }
  .tick-list .more { font-weight: 700; }

  .practice-name { position: absolute; left: 30px; top: 300px; display: flex; align-items: center; gap: 8px; font-size: 15px; font-weight: 500; color: var(--ink); }
  .practice-name__mark { width: 12px; height: 12px; background: var(--green); }
</style>
</head>
<body>
<main class="canvas">
  <p class="brief-note">i want Sizes of center banner</p>
  <p class="panel-label" style="left:40px; top:72px;">C1</p>
  <p class="panel-label" style="left:292px; top:82px;">C2</p>
  <p class="panel-label" style="left:612px; top:84px;">C3</p>
  <p class="panel-label" style="left:868px; top:83px;">C4</p>

  <svg width="0" height="0" style="position:absolute">
    <defs>
      <symbol id="tick" viewBox="0 0 12 12">
        <circle cx="6" cy="6" r="5" fill="none" stroke="var(--tick)" stroke-width="1.2"/>
        <path d="M3.6 6.2 L5.3 7.8 L8.5 4.4" fill="none" stroke="var(--tick)" stroke-width="1.3" stroke-linecap="round" stroke-linejoin="round"/>
      </symbol>
    </defs>
  </svg>

  <section class="banner banner--c1">
    <h2 class="motto">Friendly and<br>professional<br>health care<br>for <span class="accent">you</span> and<br><span class="accent">your family</span></h2>
  </section>

  <section class="banner banner--c2">
    <h2 class="offer">Bulk Billing<br>for <span class="accent">GP<br>Services</span></h2>
    <div class="booking">
      <p class="booking__lead">Book online at</p>
      <p class="booking__url">wattlebrookmedicalpractice.example.au</p>
      <p class="booking__phone">Call :&nbsp; 07 5196 4208</p>
    </div>
  </section>

  <section class="banner banner--c3">
    <div class="services">
      <h2 class="list-title">Our Services</h2>
      <ul class="tick-list">
        <li><svg><use href="#tick"/></svg>General Practice<br>Consultations</li>
        <li><svg><use href="#tick"/></svg>Immunisations</li>
        <li><svg><use href="#tick"/></svg>Health checks</li>
        <li><svg><use href="#tick"/></svg>Women’s health</li>
        <li><svg><use href="#tick"/></svg>Men’s Health</li>
        <li><svg><use href="#tick"/></svg>Skin cancer checks</li>
        <li><svg><use href="#tick"/></svg>Travel medicine</li>
        <li><svg><use href="#tick"/></svg>Referrals</li>
        <li><svg><use href="#tick"/></svg>Antenatal checks</li>
        <li><svg><use href="#tick"/></svg>Minor surgery</li>
        <li><svg><use href="#tick"/></svg>Cosmetic medicine</li>
        <li><svg><use href="#tick"/></svg>Pre Employment Medicals</li>
        <li><svg><use href="#tick"/></svg>Diabetes care</li>
        <li><svg><use href="#tick"/></svg>Wound care</li>
        <li class="more">and much more</li>
      </ul>
    </div>
  </section>

  <section class="banner banner--c4">
    <div class="allied">
      <h2 class="list-title">A Range of Allied<br>Health Services</h2>
      <ul class="tick-list">
        <li><svg><use href="#tick"/></svg>Psychology</li>
        <li><svg><use href="#tick"/></svg>Physiotherapy</li>
        <li><svg><use href="#tick"/></svg>Podiatry</li>
        <li><svg><use href="#tick"/></svg>Dietetics and Nutrition</li>
        <li><svg><use href="#tick"/></svg>Exercise Physiology</li>
        <li><svg><use href="#tick"/></svg>Diabetes Education</li>
      </ul>
    </div>
    <p class="practice-name"><span class="practice-name__mark"></span>Wattlebrook Medical Practice</p>
  </section>
</main>
</body>
</html>
```